Scrubbing Paper Towel Company needs Label Design

We need a product label that wraps around a roll of scrubbing paper towels as a sticker label of individually wrapped rolls. The sticker label has dimensions of 11.5" x 6" (width x height). The company logo with the brand feel and color theme is attached.

This is mainly used for dishwashing. A very large section of the label should show dishwashing and cleaning. Two very similar products can be found here :
---> https://www.shopvarnel.example/Non-Scratch-Disposable-Dish-Washing-Scrubbing-KT47M/dp/Q5283LRTVN/ref=sr_1_9?keywords=scouring+sheet&qid=2840175396&sr=8-9
--->https://www.shopvarnel.example/Zuvi-Flair-Disposable-Dish-washing-Scrubbing/dp/Q3961HWPXT/ref=sr_1_15?keywords=scouring+sheet&qid=2840175396&sr=8-15

To be included in the label:

Key points:
Did you know? Sponges are the perfect place for bacteria growth! We're talking hundreds of different species of bacteria growing in your dishwashing sponge - just as bad as the inside of your toilet. So why use a dirty sponge over and over again? Why does it smell so bad? Yes your toilet is gross, but why should the sponge go overlooked?

The Brisko Roll is a sanitary solution to this problem. Use it once, wash and reuse up to three times before throwing each sheet away - that's enough for 180 washes per roll! But don't limit yourself to dishwashing. It's great for scrubbing surfaces with hardened debris or even dry residue left from old spills. So go ahead, take a stand against bacteria and wash away knowing your kitchen is finally clean. Now that's sanitary!

Multipurpose Use:
Dishwashing
**(with example image/graphic)**
Cleaning Toilets
Cleaning Grills
Wiping Down Stoves
Cleaning Sinks
Cleaning Pet Bowls

60 Sheets
7.9" X 8.7" per sheet

Features:
Perforated for Easy Tear
Reusable
Liquid Absorbent
Non-Flammable
Cadmium Free
Kitchen Safe

```html
<!DOCTYPE html>
<html lang="en">
<head>
<meta charset="utf-8">
<title>Brisko Roll – Roll Label</title>
<link rel="stylesheet" href="https://fonts.googleapis.com/css2?family=Poppins:wght@500;600;700&display=swap">
<style>
  :root {
    --navy: #101c4c;
    --navy-soft: #1c2a63;
    --blue: #1f4ea3;
    --edge: #2f63c4;
    --ink: #141a3a;
    --white: #ffffff;
    --yellow: #f6e33f;
    --yellow-deep: #e2cf2a;
  }
  * { margin: 0; padding: 0; box-sizing: border-box; }
  html, body { width: 1200px; height: 626px; overflow: hidden; background: var(--white); }
  body { font-family: "Poppins", sans-serif; }
  .label { position: relative; width: 1200px; height: 626px; overflow: hidden; background: var(--white); }
  .backdrop { position: absolute; inset: 0; }

  .intro {
    position: absolute; left: 52px; top: 110px; width: 312px;
    font-size: 14px; font-weight: 600; line-height: 23.6px; color: var(--ink);
    text-align: justify; text-indent: 44px;
  }

  .features { position: absolute; left: 10px; top: 392px; width: 160px; text-align: center; color: var(--blue); }
  .features h2 { font-size: 20px; font-weight: 600; margin-bottom: 4px; }
  .features li { list-style: none; font-size: 16.5px; font-weight: 500; line-height: 20px; }

  .count { position: absolute; left: 196px; top: 394px; width: 150px; text-align: center; color: var(--blue); font-size: 16px; font-weight: 600; line-height: 22px; }

  .hand-icon { position: absolute; left: 217px; top: 460px; width: 108px; height: 108px; border-radius: 50%; border: 3px solid var(--yellow-deep); background: #fdf8d6; }

  .brand { position: absolute; left: 420px; top: 58px; width: 360px; text-align: center; color: var(--white); }
  .brand-name { font-size: 68px; font-weight: 700; line-height: 1; }
  .brand-line { font-size: 17px; font-weight: 600; margin-top: 14px; letter-spacing: 0.3px; }

  .uses { position: absolute; left: 455px; top: 357px; display: grid; grid-template-columns: 128px 128px; column-gap: 36px; row-gap: 12px; }
  .use {
    width: 128px; height: 78px; border: 1.5px solid var(--white); border-radius: 12px;
    display: flex; flex-direction: column; align-items: center; justify-content: flex-end; padding-bottom: 6px;
  }
  .use-art { width: 40px; height: 40px; border-radius: 8px; background: var(--navy-soft); border: 1px solid rgba(255,255,255,0.35); margin-bottom: 6px; }
  .use-name { color: var(--white); font-size: 10.5px; font-weight: 600; }

  .sheet-photo { position: absolute; left: 819px; top: 26px; width: 381px; height: 162px; background: linear-gradient(135deg, #f9e94e, var(--yellow) 55%, #ecd735); }

  .solution {
    position: absolute; left: 862px; top: 226px; width: 320px;
    font-size: 14px; font-weight: 600; line-height: 23.8px; color: var(--ink); text-align: justify;
  }
</style>
</head>
<body>
<main class="label">
  <svg class="backdrop" viewBox="0 0 1200 626" width="1200" height="626" aria-hidden="true">
    <path d="M0,0 L78,0 Q36,14 0,24 Z" fill="var(--navy)"/>
    <path d="M372,0 L800,0 C778,140 790,330 800,565 Q990,470 1200,492 L1200,626 L432,626 C402,420 392,210 372,0 Z" fill="var(--navy)"/>
    <path d="M372,0 C392,210 402,420 432,626" fill="none" stroke="var(--edge)" stroke-width="4"/>
    <path d="M800,0 C778,140 790,330 800,565 Q990,470 1200,492" fill="none" stroke="var(--edge)" stroke-width="4"/>
  </svg>

  <p class="intro">Did you know? Sponges are the perfect place for bacteria growth! We're talking hundreds of different species of bacteria growing in your dishwashing sponge - just as bad as the inside of your toilet. So why use a dirty sponge over and over again? Why does it smell so bad? Yes your toilet is gross, but why should the sponge go overlooked?</p>

  <section class="features">
    <h2>Features:</h2>
    <ul>
      <li>Perforated for Easy Tear</li>
      <li>Reusable</li>
      <li>Liquid Absorbent</li>
      <li>Non-Flammable</li>
      <li>Cadmium Free</li>
      <li>Kitchen Safe</li>
    </ul>
  </section>

  <p class="count">60 Sheets<br>7.9" X 8.7" per</p>
  <div class="hand-icon" role="img" aria-label="Line icon of a hand wiping with a towel"></div>

  <header class="brand">
    <div class="brand-name">Brisko Roll</div>
    <div class="brand-line">Clean Smarter, Not Harder</div>
  </header>

  <section class="uses">
    <div class="use"><div class="use-art" role="img" aria-label="Icon of a plate and sponge"></div><span class="use-name">Dishwashing</span></div>
    <div class="use"><div class="use-art" role="img" aria-label="Icon of a barbecue grill"></div><span class="use-name">Cleaning Grills</span></div>
    <div class="use"><div class="use-art" role="img" aria-label="Icon of a sparkling toilet"></div><span class="use-name">Cleaning Toilets</span></div>
    <div class="use"><div class="use-art" role="img" aria-label="Icon of a pet food bowl"></div><span class="use-name">Cleaning Pet Bowls</span></div>
    <div class="use"><div class="use-art" role="img" aria-label="Icon of a sink with faucet"></div><span class="use-name">Cleaning Sinks</span></div>
    <div class="use"><div class="use-art" role="img" aria-label="Icon of a stovetop"></div><span class="use-name">Wiping Down Stoves</span></div>
  </section>

  <div class="sheet-photo" role="img" aria-label="Close-up photo of a yellow scrubbing sheet"></div>

  <p class="solution">The Brisko Roll is a sanitary solution to this problem. Use it once, wash and reuse up to three times before throwing each sheet away - that's enough for 180 washes per roll! But don't limit yourself to dishwashing. It's great for scrubbing surfaces with hardened debris or even dry residue left from old spills. So go ahead, take a stand against bacteria and wash away knowing your kitchen is finally clean. Now that's sanitary!</p>
</main>
</body>
</html>
```